Tri fold brochure for construction company

Looking for a tri fold brochure which utilizes black, teal and white colors. Logo must be on main page (several files with Logo attached)
Inside brochure.
1st Page - 3D photo/sketch/drawing of a complete residential high rise building with windows, balconies and elements of concrete and bricks.
2nd Page - Text which will outline company's main activities. file with text is attached.
3rd Page - photo/sketch/drawing of underground parking garage which shows columns/beams/walls/ and garage entrance/exit ramp. Can be multiple photos.
Back of brochure
1st page - company logo
2nd page - please propose something.
3rd page - company message with address and contact info (to be provided)
Back ground color of brochure should complement our logo/photos/sketches/drawings.
Alternative design options are welcome.

```html
<!DOCTYPE html>
<html lang="en">
<head>
<meta charset="utf-8">
<title>Kestrel Restoration – Tri-fold Brochure</title>
<link href="https://fonts.googleapis.com/css2?family=Lato:wght@400;700;900&display=swap" rel="stylesheet">
<style>
:root{
  --teal:#1fa58f;
  --teal-dark:#178a77;
  --black:#151515;
  --white:#ffffff;
  --paper:#f6f6f4;
  --stage:#e4e4e4;
  --text:#3a3a3a;
  --muted:#9a9a9a;
}
*{box-sizing:border-box;margin:0;padding:0}
html,body{width:796px;height:1200px;overflow:hidden}
body{background:var(--stage);font-family:'Lato',sans-serif;color:var(--text);position:relative}
.spread{position:absolute;left:20px;width:756px;height:540px;display:flex;box-shadow:0 10px 28px rgba(0,0,0,.18)}
.spread--outside{top:40px}
.spread--inside{top:620px}
.panel{width:252px;height:100%;position:relative;overflow:hidden;background:var(--white);display:flex;flex-direction:column}
.panel + .panel{border-left:1px solid rgba(0,0,0,.06)}
.photo{width:100%}
.body-copy{font-size:9px;line-height:1.45}
.url-strip{height:30px;background:var(--teal);color:var(--white);font-size:10px;font-weight:700;display:flex;align-items:center;justify-content:center;letter-spacing:.3px}
.url-strip--light{background:var(--white);color:var(--black)}
/* logo */
.brand{display:flex;align-items:center;gap:8px}
.brand__mark{width:14px;height:14px;background:var(--teal)}
.brand__name{font-weight:900;font-size:17px;letter-spacing:.5px}
/* about */
.about__head{padding:18px 18px 8px}
.about__title{font-size:22px;font-weight:900;color:var(--black)}
.about__title span{color:var(--teal)}
.about__copy{padding:0 18px 12px}
.about__dark{background:var(--black);color:#ddd;padding:16px 18px;flex:1}
/* middle outside */
.message{background:var(--teal);color:var(--white);height:120px;text-align:center;padding-top:26px;position:relative}
.message h2{font-size:19px;font-weight:900;line-height:1.2}
.contact{background:var(--black);padding:26px 22px 20px;flex:1;display:flex;flex-direction:column;gap:16px}
.contact__row{display:flex;align-items:center;gap:12px;color:#e8e8e8;font-size:10px}
.contact__icon{width:26px;height:26px;border-radius:50%;background:var(--teal);display:flex;align-items:center;justify-content:center;flex:none}
.logo-block{height:90px;display:flex;align-items:center;justify-content:center}
.logo-block .brand__name{color:var(--black)}
.call{background:var(--teal);color:var(--white);text-align:center;padding:14px 0 16px}
.call__label{font-size:16px;font-weight:700}
.call__number{font-size:21px;font-weight:900;letter-spacing:.5px;margin-top:2px}
/* cover */
.cover__top{background:var(--black);height:120px;display:flex;align-items:center;justify-content:center}
.cover__top .brand__name{color:var(--white)}
.cover__headline{background:var(--teal);color:var(--white);text-align:center;padding:26px 14px;font-size:22px;font-weight:900;line-height:1.2}
/* inside left */
.inside-left__bar{height:34px;background:var(--teal)}
.inside-left__copy{padding:16px 18px 14px}
/* services */
.services{background:var(--black);padding:18px 14px 14px;color:#e8e8e8}
.section-title{font-size:14px;font-weight:900;color:var(--teal);text-align:center;margin-bottom:10px}
.cols{display:grid;grid-template-columns:1fr 1fr;gap:8px 10px}
.tag{display:inline-block;background:var(--teal);color:var(--white);font-size:7.5px;font-weight:900;text-transform:uppercase;padding:3px 7px;border-radius:8px;margin-bottom:4px}
.list{list-style:none;font-size:8px;line-height:1.5}
.list li{display:flex;gap:5px;align-items:flex-start}
.list li::before{content:"";flex:none;width:7px;height:7px;border-radius:50%;background:var(--teal);margin-top:3px}
.garage{padding:14px 14px 12px;flex:1;color:var(--text)}
/* inside right */
.misc{background:var(--teal);color:var(--white);margin:0 0;padding:16px 18px;}
.misc h3{font-size:15px;font-weight:900;margin-bottom:8px}
.misc .list li::before{background:var(--white)}
.misc .list{font-size:8.5px}
.call--plain{background:var(--white);color:var(--teal);text-align:left;padding:18px 18px}
.call--plain .call__number{color:var(--teal)}
</style>
</head>
<body>

<!-- OUTSIDE -->
<section class="spread spread--outside">
  <article class="panel about">
    <header class="about__head"><h2 class="about__title">About <span>Us</span></h2></header>
    <p class="body-copy about__copy">We are a family run restoration firm serving owners and boards for over twenty years. Our crews repair, protect and renew concrete, masonry and facades on towers across the city.</p>
    <div class="photo" role="img" aria-label="Photo of a worker with a tool belt and hard hat on a job site" style="height:150px;background:linear-gradient(160deg,#c9c6c0,#7e7a73 60%,#3c3a36)"></div>
    <p class="body-copy about__dark">Every project starts with a careful survey and a clear plan. We keep residents informed, work safely around daily life and leave each building stronger than we found it, backed by a written warranty on all work.</p>
    <div class="url-strip">www.kestrelrestoration.com</div>
  </article>

  <article class="panel">
    <div class="message">
      <h2>Your company<br>message<br>Will Goes Here</h2>
    </div>
    <svg width="252" height="16" viewBox="0 0 252 16" style="display:block;background:var(--black)" aria-hidden="true"><path d="M0 0H252V4Q126 20 0 4Z" fill="#1fa58f"/></svg>
    <div class="contact">
      <div class="contact__row"><span class="contact__icon"><svg width="12" height="12" viewBox="0 0 24 24"><path fill="#fff" d="M6.6 10.8a15 15 0 0 0 6.6 6.6l2.2-2.2a1 1 0 0 1 1-.25 11 11 0 0 0 3.6.6 1 1 0 0 1 1 1V20a1 1 0 0 1-1 1A17 17 0 0 1 3 4a1 1 0 0 1 1-1h3.5a1 1 0 0 1 1 1c0 1.25.2 2.45.6 3.6a1 1 0 0 1-.25 1z"/></svg></span>+01 555 204 118</div>
      <div class="contact__row"><span class="contact__icon"><svg width="12" height="12" viewBox="0 0 24 24"><rect x="3" y="5" width="18" height="14" rx="1.5" fill="#fff"/><path d="M3.5 6l8.5 7 8.5-7" stroke="#1fa58f" stroke-width="2" fill="none"/></svg></span>hello@kestrelrestoration.com</div>
      <div class="contact__row"><span class="contact__icon"><svg width="12" height="12" viewBox="0 0 24 24" fill="none" stroke="#fff" stroke-width="2"><circle cx="12" cy="12" r="9"/><path d="M3 12h18M12 3c3 3 3 15 0 18M12 3c-3 3-3 15 0 18"/></svg></span>kestrelrestoration.com</div>
      <div class="contact__row"><span class="contact__icon"><svg width="12" height="12" viewBox="0 0 24 24"><path fill="#fff" d="M12 2a7 7 0 0 0-7 7c0 5 7 13 7 13s7-8 7-13a7 7 0 0 0-7-7zm0 9.5A2.5 2.5 0 1 1 12 6.5a2.5 2.5 0 0 1 0 5z"/></svg></span>125 Harbour Street,<br>Suite 4, Lakeview</div>
    </div>
    <div class="logo-block"><div class="brand"><span class="brand__mark"></span><span class="brand__name">KESTREL RESTORATION</span></div></div>
    <div class="call"><div class="call__label">Call Us Today</div><div class="call__number">00 321 654 0987</div></div>
  </article>

  <article class="panel">
    <div class="cover__top"><div class="brand"><span class="brand__mark"></span><span class="brand__name">KESTREL RESTORATION</span></div></div>
    <div class="photo" role="img" aria-label="Aerial photo of a city skyline of high rise towers at sunset" style="height:200px;background:linear-gradient(180deg,#b9c3c6,#9c8f78 45%,#5a5346 80%,#2e2c28)"></div>
    <div class="cover__headline">Your Headline<br>Will Goes Here</div>
    <div style="flex:1"></div>
    <div class="url-strip url-strip--light">www.kestrelrestoration.com</div>
  </article>
</section>

<!-- INSIDE -->
<section class="spread spread--inside">
  <article class="panel">
    <div class="inside-left__bar"></div>
    <p class="body-copy inside-left__copy">From balcony slabs to parking decks, our teams handle the full life of a concrete structure. We assess damage, design lasting repairs and finish on time, keeping your residents safe and your property value high for years to come.</p>
    <div class="photo" role="img" aria-label="Photo of a modern residential high rise with balconies and blue glass" style="flex:1;background:linear-gradient(180deg,#e4e6e8,#bcc3c8 40%,#6f8aa3 70%,#4d5e4a)"></div>
  </article>

  <article class="panel">
    <div class="services">
      <h3 class="section-title">Building Envelope</h3>
      <div class="cols">
        <div><span class="tag">Facade Repairs</span><ul class="list"><li>Concrete patching</li><li>Crack injection</li><li>Sealant renewal</li></ul></div>
        <div><span class="tag">Masonry</span><ul class="list"><li>Brick relaying</li><li>Repointing joints</li><li>Lintel renewal</li></ul></div>
        <div><span class="tag">Balcony Repairs</span><ul class="list"><li>Slab edge rebuild</li><li>Railing anchors</li><li>Deck membranes</li></ul></div>
        <div><span class="tag">Waterproofing</span><ul class="list"><li>Roof and terrace</li><li>Coatings and sealers</li></ul></div>
      </div>
    </div>
    <div class="garage">
      <h3 class="section-title">Parking Garage Structures</h3>
      <div class="cols">
        <div><span class="tag">Concrete Repairs</span><ul class="list"><li>Partial depth repair</li><li>Column and beam jackets</li><li>Ramp resurfacing</li></ul></div>
        <div><span class="tag">Protection</span><ul class="list"><li>Traffic membranes</li><li>Expansion joints</li><li>Line painting</li></ul></div>
        <div><span class="tag">Drainage</span><ul class="list"><li>Electric heating cables</li><li>Slab drains</li></ul></div>
        <div><span class="tag">Structural</span><ul class="list"><li>Crystalline waterproofing</li></ul></div>
      </div>
    </div>
  </article>

  <article class="panel">
    <div class="photo" role="img" aria-label="Photo of an underground parking garage with columns, parked cars and ramp" style="height:190px;background:linear-gradient(170deg,#d5d5d5,#8f8f8f 50%,#3e3e3e)"></div>
    <div class="misc">
      <h3>Miscellaneous</h3>
      <ul class="list">
        <li>Structural steel painting</li>
        <li>Epoxy floor coatings</li>
        <li>Stair and landing repairs</li>
        <li>Plaza deck renewal</li>
        <li>Condition surveys</li>
        <li>Emergency shoring</li>
      </ul>
    </div>
    <div class="call call--plain"><div class="call__label">Call Us Today</div><div class="call__number">00 321 654 0987</div></div>
  </article>
</section>

</body>
</html>
```